Consulting company needs Business Cards - rough concept provided

I'm looking for someone to take our business card idea and make is slick and polished - to communicate our high-end, sophisticated, serious consulting business. We have a rough layout we did in-house. We are open to ideas on repo-ing elements, adjusting sizes, typefaces etc... within the general concept we've already come up with. We want it to be super-clean and sophisticated. We want to keep the white backgrounds, and blue brand colors. Our goal is to print with painted blue edges on thick cardstock. Thank you!!

```html
<!DOCTYPE html>
<html lang="en">
<head>
<meta charset="utf-8">
<title>Tallfern Business Card</title>
<link rel="stylesheet" href="https://fonts.googleapis.com/css2?family=Montserrat:ital,wght@0,400;0,800;1,400&family=Lato:wght@400&family=Poppins:wght@700&family=Quicksand:wght@300&display=swap">
<style>
  :root {
    --stage: #1b1b1c;
    --card-white: #ffffff;
    --card-shade: #e4e4e6;
    --brand-blue: #1fa3de;
    --brand-blue-deep: #168fcf;
    --brand-blue-soft: #45a6d4;
    --wordmark-blue: #a9e2f7;
    --ink: #1d1d1f;
    --ink-soft: #3a3a3d;
    --back-text: rgba(225, 242, 252, 0.8);
  }
  * { margin: 0; padding: 0; box-sizing: border-box; }
  html, body {
    width: 1200px;
    height: 915px;
    overflow: hidden;
    background: var(--stage);
  }
  .stage {
    position: relative;
    width: 1200px;
    height: 915px;
    display: flex;
    flex-direction: column;
    align-items: center;
    justify-content: center;
    gap: 56px;
  }
  .card {
    position: relative;
    width: 640px;
    height: 366px;
    overflow: hidden;
    border-radius: 2px;
  }

  /* Front side */
  .card-front {
    background: radial-gradient(ellipse at 35% 35%, var(--card-white) 45%, var(--card-shade) 100%);
    border-bottom: 3px solid var(--brand-blue);
  }
  .wordmark {
    position: absolute;
    top: 10px;
    left: 0;
    width: 100%;
    text-align: center;
    font-family: "Montserrat", sans-serif;
    font-weight: 800;
    font-size: 106px;
    letter-spacing: -2px;
    line-height: 1;
    color: var(--wordmark-blue);
    white-space: nowrap;
  }
  .person {
    position: absolute;
    left: 64px;
    top: 168px;
    font-family: "Montserrat", sans-serif;
    color: var(--ink);
  }
  .person-name {
    font-size: 21px;
    font-weight: 400;
    letter-spacing: 0.3px;
  }
  .person-name .first { font-weight: 800; }
  .person-role {
    font-size: 14px;
    font-style: italic;
    color: var(--ink-soft);
    margin-top: 1px;
  }
  .contact {
    position: absolute;
    left: 330px;
    top: 250px;
    font-family: "Lato", sans-serif;
    font-size: 16px;
    color: var(--ink-soft);
    letter-spacing: 0.6px;
    list-style: none;
  }
  .contact-item {
    display: flex;
    align-items: flex-start;
    gap: 8px;
    line-height: 1.3;
    margin-bottom: 5px;
  }
  .contact-icon {
    flex: none;
    width: 15px;
    height: 15px;
    margin-top: 3px;
  }

  /* Back side */
  .card-back {
    background: linear-gradient(200deg, var(--brand-blue) 0%, var(--brand-blue-deep) 50%, var(--brand-blue-soft) 100%);
    padding: 50px 44px;
    font-size: 29px;
    line-height: 1.6;
    color: var(--back-text);
  }
  .mission {
    font-family: "Quicksand", sans-serif;
    font-weight: 300;
  }
  .mission .line { display: block; white-space: nowrap; }
  .mission strong {
    font-family: "Poppins", sans-serif;
    font-weight: 700;
    font-size: 27px;
  }
</style>
</head>
<body>
<main class="stage">

  <section class="card card-front" aria-label="Business card front">
    <div class="wordmark">TALLFERN</div>

    <div class="person">
      <p class="person-name"><span class="first">Dana</span>Whitlock</p>
      <p class="person-role">Brand Consultant</p>
    </div>

    <ul class="contact">
      <li class="contact-item">
        <svg class="contact-icon" viewBox="0 0 16 16" aria-hidden="true">
          <circle cx="8" cy="8" r="8" fill="var(--brand-blue)"/>
          <path d="M8 3.6a2.9 2.9 0 0 0-2.9 2.9c0 2.1 2.9 5.6 2.9 5.6s2.9-3.5 2.9-5.6A2.9 2.9 0 0 0 8 3.6z" fill="#fff"/>
          <circle cx="8" cy="6.5" r="1.1" fill="var(--brand-blue)"/>
        </svg>
        <span>4820 Harbor Lane, Ste 210<br>Brookvale, CA 90412</span>
      </li>
      <li class="contact-item">
        <svg class="contact-icon" viewBox="0 0 16 16" aria-hidden="true">
          <circle cx="8" cy="8" r="8" fill="var(--brand-blue)"/>
          <path d="M5.3 4.2l1.4-.4.9 2-1 .8a5.5 5.5 0 0 0 2.8 2.8l.8-1 2 .9-.4 1.4c-3.8.3-6.8-2.7-6.5-6.5z" fill="#fff"/>
        </svg>
        <span>(555) 214 7730</span>
      </li>
      <li class="contact-item">
        <svg class="contact-icon" viewBox="0 0 16 16" aria-hidden="true">
          <circle cx="8" cy="8" r="8" fill="var(--brand-blue)"/>
          <rect x="4" y="5.2" width="8" height="5.6" rx="0.6" fill="#fff"/>
          <path d="M4.3 5.6L8 8.4l3.7-2.8" fill="none" stroke="var(--brand-blue)" stroke-width="0.9"/>
        </svg>
        <span>dana@tallfern.com</span>
      </li>
    </ul>
  </section>

  <section class="card card-back" aria-label="Business card back">
    <p class="mission">
      <span class="line"><strong>We help</strong> [target demographic] <strong>achieve</strong></span>
      <span class="line">[desired emotional outcome] <strong>by</strong></span>
      <span class="line">[ourunique approach] <strong>because</strong></span>
      <span class="line">[our brand beliefs]</span>
    </p>
  </section>

</main>
</body>
</html>
```